Family Owned Construction Company Needs Modern Business Cards

We need a new design for our business cards. We are a family owned construction company, Torvane Construction, based in Mendon, Vermont and would like to add in our new logo and find a more modern look. We also want to use our old to make sure people know who we are. We do site development, highway, environmental, demolition, utility and aggregate.

Contact Information for Business Card

We want to have the office address, 48 Millbrook Road, Kelmont, NA 05719 and our phone (802) 555-0148 and fax (802) 555-0193 on there as well. Our website is www.torvaneinc.example. There should be a place for the person's name, title, cell number, and email address on the card. Words that we would like to be associated with our company are honesty, predictable, reliable, integrity, dedicated, built right quality, consistent, whatever it takes, and innovation. Safety is also very important to us.

Font styles to use
Serif
Sans Serif
Other font styles liked:
• Square 721 Extented

Colors
0255a3
ffffff

Requirements
Must have
• Office address, phone number and fax number. New logo with excavator
Nice to have
• That we do site development, highway, environmental, demolition, utility, and aggregate. Both logos

```html
<!DOCTYPE html>
<html lang="en">
<head>
<meta charset="utf-8">
<title>Torvane Construction – Business Cards</title>
<link rel="stylesheet" href="https://fonts.googleapis.com/css2?family=Poppins:wght@500;600&family=Work+Sans:wght@400;500;700&display=swap">
<style>
  :root {
    --navy: #1b3361;
    --white: #ffffff;
    --ink: #2d2d2d;
    --grey-text: #555a60;
    --rule: #3a3a3a;
    --stage: #e4e4e4;
  }
  * { margin: 0; padding: 0; box-sizing: border-box; }
  html, body { width: 1200px; height: 1000px; overflow: hidden; }
  body {
    background: var(--stage);
    font-family: "Work Sans", Arial, sans-serif;
    display: flex;
    align-items: center;
    justify-content: center;
    gap: 40px;
  }
  .card {
    position: relative;
    width: 560px;
    height: 340px;
    overflow: hidden;
    box-shadow: 0 6px 18px rgba(0,0,0,0.22);
  }

  /* Front */
  .card-front { background: var(--white); color: var(--ink); }
  .wordmark {
    position: absolute;
    left: 36px; top: 34px;
    font-family: "Work Sans", Arial, sans-serif;
    font-weight: 700;
    color: var(--navy);
    text-transform: uppercase;
    line-height: 1.05;
  }
  .wordmark .word-main { display: block; font-size: 34px; letter-spacing: 1px; }
  .wordmark .word-sub { display: block; font-size: 13px; letter-spacing: 1.5px; }

  .side-tab {
    position: absolute;
    left: -8px; top: 166px;
    width: 16px; height: 32px;
    background: var(--navy);
    border-radius: 6px;
  }
  .person-name {
    position: absolute;
    left: 36px; top: 164px;
    font-family: "Poppins", Arial, sans-serif;
    font-weight: 600;
    font-size: 19px;
    color: var(--navy);
  }
  .person-title {
    position: absolute;
    left: 36px; top: 190px;
    font-family: "Poppins", Arial, sans-serif;
    font-weight: 500;
    font-size: 13px;
    color: var(--grey-text);
  }
  .name-rule {
    position: absolute;
    left: 172px; right: 0; top: 204px;
    height: 2px;
    background: var(--rule);
  }
  .brand-square {
    position: absolute;
    right: 40px; top: 108px;
    display: flex; flex-direction: column; align-items: center; gap: 6px;
  }
  .brand-square .square {
    width: 70px; height: 62px;
    background: var(--navy);
    border-radius: 6px;
  }
  .brand-square .label {
    font-weight: 700; font-size: 8px; letter-spacing: 0.6px;
    color: var(--navy); text-transform: uppercase;
  }

  .contact-list {
    position: absolute;
    left: 36px; top: 222px;
    list-style: none;
    font-size: 11.5px;
    line-height: 17px;
    color: var(--ink);
  }
  .contact-list li { display: flex; align-items: center; gap: 9px; }
  .contact-list svg { width: 9px; height: 9px; fill: var(--navy); flex: none; }

  .address {
    position: absolute;
    right: 28px; top: 276px;
    font-size: 11.5px;
    line-height: 16px;
    color: var(--ink);
    letter-spacing: 0.3px;
  }
  .footer-band {
    position: absolute;
    left: 0; right: 0; bottom: 0;
    height: 22px;
    background: var(--navy);
  }
  .footer-band .gap {
    position: absolute;
    left: 358px; top: -2px;
    width: 4px; height: 30px;
    background: var(--white);
    transform: skewX(-25deg);
  }

  /* Back */
  .card-back {
    background: var(--navy);
    color: var(--white);
    display: flex; flex-direction: column; align-items: center;
  }
  .card-back .wordmark {
    position: static;
    margin-top: 122px;
    color: var(--white);
    text-align: center;
  }
  .services {
    margin-top: 74px;
    text-align: center;
    font-size: 10.5px;
    line-height: 16px;
    letter-spacing: 0.3px;
  }
</style>
</head>
<body>

  <section class="card card-front" aria-label="Business card front">
    <div class="wordmark">
      <span class="word-main">Torvane</span>
      <span class="word-sub">Construction Inc.</span>
    </div>

    <div class="brand-square">
      <div class="square"></div>
      <div class="label">Construction Inc.</div>
    </div>

    <div class="side-tab"></div>
    <div class="person-name">Dorian Vell</div>
    <div class="person-title">Founder</div>
    <div class="name-rule"></div>

    <ul class="contact-list">
      <li>
        <svg viewBox="0 0 10 10"><path d="M1 3 Q5 0 9 3 L8 4.5 L6.5 3.6 L3.5 3.6 L2 4.5 Z M2.5 5 H7.5 L8.5 9 H1.5 Z"/></svg>
        (802) 555-0148
      </li>
      <li>
        <svg viewBox="0 0 10 10"><rect x="1" y="4" width="8" height="5"/><rect x="3" y="1" width="4" height="3"/></svg>
        (802) 555-0193
      </li>
      <li>
        <svg viewBox="0 0 10 10"><path d="M0.5 2 H9.5 V8.5 H0.5 Z M1 2.5 L5 5.5 L9 2.5" stroke="#fff" stroke-width="0.8"/></svg>
        info@dvell.example
      </li>
      <li>
        <svg viewBox="0 0 10 10"><circle cx="5" cy="5" r="4.5"/></svg>
        torvaneinc.example
      </li>
    </ul>

    <div class="address">48 Millbrook Road,<br>Kelmont, NA 05719</div>

    <div class="footer-band"><span class="gap"></span></div>
  </section>

  <section class="card card-back" aria-label="Business card back">
    <div class="wordmark">
      <span class="word-main">Torvane</span>
      <span class="word-sub">Construction Inc.</span>
    </div>
    <p class="services">
      site development | highway<br>
      environmental | demolition | utility | aggregate
    </p>
  </section>

</body>
</html>
```